Briefbogen und Visitenkarte für Grundstücksverwaltunggesellschaft
Zielgruppe
Wir sind eine Grundstücksverwaltungsgesellschaft und Verwalten eine Vielzahl an Logistik- und Industrieimmobilien.
Aufgabenstellung
Wir bitten um Verwendung unseres Logo, siehe Anlage. Die Bildmarke darf nicht verändert werden, die Wortmarke darf unter Umständen otimiert werden.
Wir möchten einen dezenten Auftritt vermitteln und bitten daher um graue Schrift als Grundfarbe.
Bei der Visitenkarte könnten wir uns eine einfarbig blaue Rückseite vorstellen.
Folgende Daten kommen zur Verwendung:
Lindwerk Grundstücksverwaltungs GmbH
Internet: www.lindwerk-grundbesitz.de

```html
<!DOCTYPE html>
<html lang="de">
<head>
<meta charset="utf-8">
<title>Lindwerk Grundstücksverwaltungs GmbH – Geschäftsausstattung</title>
<link rel="stylesheet" href="https://fonts.googleapis.com/css2?family=Open+Sans:wght@300;400;600&display=swap">
<style>
  :root {
    --bg: #8f8f8f;
    --paper: #f4f4f4;
    --ink: #1f1f1f;
    --grey-text: #7a7a7a;
    --brand-grey: #808080;
    --brand-blue: #004a80;
    --rule-blue: #2f6aa0;
  }
  * { box-sizing: border-box; margin: 0; padding: 0; }
  html, body { width: 1200px; height: 720px; overflow: hidden; }
  body {
    position: relative;
    background: var(--bg);
    font-family: "Open Sans", Arial, sans-serif;
    color: var(--ink);
  }
  .sheet {
    position: absolute;
    background: var(--paper);
    box-shadow: 0 1px 4px rgba(0,0,0,.18);
  }

  /* brand name block */
  .brand { position: absolute; color: var(--brand-grey); font-weight: 400; white-space: nowrap; line-height: 1.15; }
  .brand-name { display: block; }
  .brand-sub { display: block; }

  /* letterhead */
  .letterhead { left: 258px; top: 52px; width: 413px; height: 584px; }
  .letterhead .brand { right: 20px; top: 42px; text-align: right; }
  .letterhead .brand-name { font-size: 12px; letter-spacing: .06em; }
  .letterhead .brand-sub { font-size: 5.2px; letter-spacing: .05em; }
  .sender-line { position: absolute; left: 40px; top: 99px; font-size: 4px; color: var(--grey-text); }
  .sender-line strong { color: var(--ink); font-weight: 600; }
  .fold-mark { position: absolute; left: 0; width: 6px; height: 0; border-top: .5px solid #bbb; }
  .letter-body { position: absolute; left: 40px; top: 231px; width: 335px; }
  .letter-title { font-size: 11px; font-weight: 600; margin-bottom: 12px; }
  .letter-body p { font-size: 6.2px; line-height: 13px; margin-bottom: 13px; }
  .closing { font-size: 6.2px; line-height: 8.2px; }
  .letter-footer { position: absolute; left: 40px; top: 553px; display: flex; gap: 8px; }
  .footer-col { border-left: 1px solid var(--rule-blue); padding-left: 3px; font-size: 4.3px; line-height: 6.1px; color: var(--grey-text); white-space: nowrap; }
  .footer-col:nth-child(1) { width: 78px; }
  .footer-col:nth-child(2) { width: 97px; }
  .footer-col:nth-child(3) { width: 85px; }

  /* business card */
  .card { width: 167px; height: 106px; left: 705px; }
  .card-front { top: 113px; background: linear-gradient(115deg, #f2f2f2 0%, #e6e6e6 60%, #f3f3f3 100%); }
  .card-front .brand { left: 14px; top: 20px; }
  .card-front .brand-name { font-size: 9px; letter-spacing: .06em; }
  .card-front .brand-sub { font-size: 4px; letter-spacing: .04em; }
  .card-person { position: absolute; left: 14px; top: 55px; color: var(--grey-text); }
  .card-name { font-size: 6.6px; font-weight: 300; }
  .card-role { font-size: 3.8px; }
  .card-contact { position: absolute; left: 14px; top: 72px; font-size: 3.9px; line-height: 6.1px; color: var(--grey-text); }
  .card-back { top: 245px; background: var(--brand-blue); display: flex; align-items: center; justify-content: center; box-shadow: none; }
  .card-back .back-name { color: #fff; font-size: 10px; letter-spacing: .08em; }

  /* compliment envelope */
  .envelope { left: 708px; top: 407px; width: 393px; height: 196px; }
  .envelope .brand { left: 53px; top: 18px; }
  .envelope .brand-name { font-size: 10px; letter-spacing: .06em; }
  .envelope .brand-sub { font-size: 4.4px; letter-spacing: .05em; }
</style>
</head>
<body>

  <section class="sheet letterhead" aria-label="Briefbogen">
    <div class="brand">
      <span class="brand-name">Lindwerk</span>
      <span class="brand-sub">Grundstücksverwaltungs GmbH</span>
    </div>
    <p class="sender-line"><strong>Lindwerk</strong> Grundstücksverwaltungs GmbH · Werftgasse 8 · 23560 Lübeck</p>
    <span class="fold-mark" style="top:206px"></span>
    <span class="fold-mark" style="top:292px;width:14px"></span>

    <div class="letter-body">
      <h1 class="letter-title">Donec sodales sagittis magna.</h1>
      <p>Lorem ipsum dolor sit amet, consectetuer adipiscing elit. Aenean commodo ligula eget dolor. Aenean massa. Cum sociis natoque penatibus et magnis dis parturient montes, nascetur ridiculus mus. Donec quam felis, ultricies nec, pellentesque eu, pretium quis, sem. Nulla consequat massa quis enim. Donec pede justo, fringilla vel, aliquet nec, vulputate eget, arcu. In enim justo, rhoncus ut, imperdiet a, venenatis vitae, justo.</p>
      <p>Nullam dictum felis eu pede mollis pretium. Integer tincidunt. Cras dapibus. Vivamus elementum semper nisi. Aenean vulputate eleifend tellus. Aenean leo ligula, porttitor eu, consequat vitae, eleifend ac, enim. Aliquam lorem ante, dapibus in, viverra quis, feugiat a, tellus. Phasellus viverra nulla ut metus varius laoreet. Quisque rutrum. Aenean imperdiet. Etiam ultricies nisi vel augue. Curabitur ullamcorper ultricies nisi. Nam eget dui. Etiam rhoncus. Maecenas tempus, tellus eget condimentum rhoncus, sem quam semper libero, sit amet adipiscing sem neque sed ipsum. Nam quam nunc, blandit vel, luctus pulvinar, hendrerit id, lorem. Maecenas nec odio et ante tincidunt tempus.</p>
      <div class="closing">
        Mit freundlichen Grüßen<br>
        Jonas Behrendt<br>
        Lindwerk<br>
        Grundstücksverwaltungs GmbH
      </div>
    </div>

    <footer class="letter-footer">
      <div class="footer-col">Lindwerk<br>Grundstücksverwaltungs GmbH<br>Werftgasse 8<br>23560 Lübeck</div>
      <div class="footer-col">Telefon: 0451-482110-0<br>Telefax: 0451-482110-29<br>info@lindwerk-grundbesitz.de<br>www.lindwerk-grundbesitz.de</div>
      <div class="footer-col">Geschäftsführer: Jonas Behrendt<br>USt.IDNr.: DE318775064<br>Steuernummer: 22 417 30962<br>Amtsgericht Lübeck · HRB 7481 HL</div>
      <div class="footer-col">Bankverbindung:<br>Hansebank Nord AG<br>IBAN: DE12 2304 0000 0048 2110 07<br>BIC: HBNODE21XXX</div>
    </footer>
  </section>

  <section class="sheet card card-front" aria-label="Visitenkarte Vorderseite">
    <div class="brand">
      <span class="brand-name">Lindwerk</span>
      <span class="brand-sub">Grundstücksverwaltungs GmbH</span>
    </div>
    <div class="card-person">
      <div class="card-name">Jonas Behrendt</div>
      <div class="card-role">Geschäftsführer</div>
    </div>
    <div class="card-contact">
      Werftgasse 8 · 23560 Lübeck<br>
      Telefon 0451-482110-0 · Mobil 0171-5527340<br>
      j.behrendt@lindwerk-grundbesitz.de<br>
      www.lindwerk-grundbesitz.de
    </div>
  </section>

  <section class="sheet card card-back" aria-label="Visitenkarte Rückseite">
    <span class="back-name">Lindwerk</span>
  </section>

  <section class="sheet envelope" aria-label="Kuvert">
    <div class="brand">
      <span class="brand-name">Lindwerk</span>
      <span class="brand-sub">Grundstücksverwaltungs GmbH</span>
    </div>
  </section>

</body>
</html>
```